Free wellness evaluation

We need an A5 flyer designing using both sides The front side needs to contain most of the information about the free wellness evaluation with Voucher clearly Displayed,we needs to demonstrate that we are very professional company offering a unique service

Industry/Entity Type

Wellness

```html
<!DOCTYPE html>
<html lang="en">
<head>
<meta charset="utf-8">
<title>Free Wellness Evaluation Flyer</title>
<link rel="stylesheet" href="https://fonts.googleapis.com/css2?family=Fira+Sans:ital,wght@0,600;1,400;1,500;1,600;1,700&display=swap">
<style>
  :root {
    --backdrop-centre: #7d8483;
    --backdrop-edge: #0b0d0d;
    --paper: #ffffff;
    --ink: #1a1a1a;
    --orange: #ff8200;
    --green: #4ccf0a;
    --footer: #1c1c1c;
    --footer-text: #cfcfcf;
    --white: #ffffff;
  }
  * { margin: 0; padding: 0; box-sizing: border-box; }
  html, body { width: 1200px; height: 1000px; overflow: hidden; }
  body {
    background: radial-gradient(ellipse 560px 620px at 600px 500px, var(--backdrop-centre) 0%, #3c4242 45%, var(--backdrop-edge) 100%);
    font-family: "Fira Sans", sans-serif;
    font-style: italic;
    color: var(--ink);
    position: relative;
  }
  .flyer {
    position: absolute; left: 288px; top: 58px;
    width: 622px; height: 882px;
    background: var(--paper);
  }
  .flyer > * { position: absolute; }
  .section-title {
    font-weight: 500; font-size: 29.5px; color: var(--orange);
    line-height: 1; white-space: nowrap;
  }
  .checklist { list-style: none; font-size: 18.5px; line-height: 23px; white-space: nowrap; }
  .checklist li { position: relative; padding-left: 15px; }
  .bullet-text { padding-left: 15px; font-size: 18.5px; line-height: 23.5px; white-space: nowrap; }
  .chevron {
    position: absolute; left: 0; top: 7px; width: 8px; height: 10px;
  }
  .voucher-title {
    left: 0; width: 622px; text-align: center;
    font-weight: 600; font-size: 37px; color: var(--green); letter-spacing: -0.5px;
  }
  .voucher-booking {
    left: 0; width: 622px; text-align: center; font-size: 17px; line-height: 21px;
  }
  .voucher-booking b { font-weight: 600; }
  .voucher-note {
    left: 0; width: 622px; text-align: center;
    font-weight: 700; font-size: 20.5px; letter-spacing: -0.3px;
  }
  .contact-band {
    left: 0; top: 711px; width: 622px; height: 171px;
    background: var(--footer);
  }
  .contact-band > * { position: absolute; }
  .contact-title { left: 21px; top: 14px; font-weight: 500; font-size: 26px; color: var(--white); }
  .brand {
    right: 10px; top: 10px; display: flex; align-items: center; gap: 6px;
    font-style: normal; font-weight: 600; font-size: 16px; color: var(--white); letter-spacing: 0.2px;
  }
  .brand-dot { width: 20px; height: 20px; border-radius: 50%; background: var(--white); }
  .location { left: 21px; top: 56px; font-size: 18px; line-height: 23px; color: var(--footer-text); white-space: nowrap; }
  .location b { font-weight: 600; }
  .directions { left: 21px; top: 134px; font-size: 21px; color: var(--white); letter-spacing: -0.3px; white-space: nowrap; }
  .directions b { font-weight: 700; }
</style>
</head>
<body>
<svg width="0" height="0" style="position:absolute">
  <defs>
    <symbol id="chev" viewBox="0 0 8 10"><path d="M1.5 1 L6 5 L1.5 9" fill="none" stroke="#4ccf0a" stroke-width="2.4"/></symbol>
  </defs>
</svg>

<main class="flyer">
  <h2 class="section-title" style="left:55px;top:28px;">Free wellness evaluation covers</h2>
  <ul class="checklist" style="left:68px;top:75px;">
    <li><svg class="chevron"><use href="#chev"/></svg>Consultation</li>
    <li><svg class="chevron"><use href="#chev"/></svg>Diet review</li>
    <li><svg class="chevron"><use href="#chev"/></svg>Advice on any changes</li>
    <li><svg class="chevron"><use href="#chev"/></svg>Testing of-Body fat %</li>
    <li><svg class="chevron"><use href="#chev"/></svg>Muscle mass</li>
    <li><svg class="chevron"><use href="#chev"/></svg>Bone mess</li>
  </ul>
  <ul class="checklist" style="left:344px;top:75px;">
    <li><svg class="chevron"><use href="#chev"/></svg>Body mass index (BMI)</li>
    <li><svg class="chevron"><use href="#chev"/></svg>Basal Metabolic rate</li>
    <li><svg class="chevron"><use href="#chev"/></svg>Metabolic age</li>
    <li><svg class="chevron"><use href="#chev"/></svg>body water %</li>
    <li><svg class="chevron"><use href="#chev"/></svg>Visceral fat</li>
    <li><svg class="chevron"><use href="#chev"/></svg>Blood pressure</li>
  </ul>

  <h2 class="section-title" style="left:53px;top:237px;">Free fit club</h2>
  <p class="bullet-text" style="left:65px;top:280px;"><svg class="chevron"><use href="#chev"/></svg>Join a friendly group of people for fun, simple<br>and brilliant group exercise non military boot camp,<br>and then join us for a recovery shake and weekly<br>nutrition topic</p>

  <h2 class="section-title" style="left:56px;top:389px;">Business opportunity</h2>
  <p class="bullet-text" style="left:65px;top:422px;"><svg class="chevron"><use href="#chev"/></svg>If you're interested in exciting new business opportunities<br>with great financial awards this is simply an opportunity<br>for anyone Who is looking to supplement their income.<br>Contact our business development team on:<br><b style="font-weight:600">startup@vitalityworkscentre.co.uk</b></p>

  <h2 class="voucher-title" style="top:548px;">Voucher</h2>
  <p class="voucher-booking" style="top:596px;">Please book your wellness evaluation at:<br>www.<b>vitalityworkscentre.co.uk</b>/freewellness<br>Or email <b>booking@vitalityworkscentre.co.uk</b></p>
  <p class="voucher-note" style="top:674px;">Please bring voucher to your wellness evaluation.</p>

  <footer class="contact-band">
    <h2 class="contact-title">Find or Contact Us</h2>
    <div class="brand"><span class="brand-dot"></span>VITALITY WORKS</div>
    <p class="location">Find the, Vitality Works Centre <b>Eastbrook</b><br>The centre is located above the Market Lane entrance on Bridge<br>Street, in the centre of Eastbrook.</p>
    <p class="directions">Please contact your coach or us on <b>07700900123</b> for directions</p>
  </footer>
</main>
</body>
</html>
```